Website design for Nutraceutical Contract Manufacturer in NJ

Develop website for a contract manufacturer, specializing in nutraceutical products. Our color theme is based on the colors of the American flag (Pantone blue no. 282 & red no. 193, white), representing a US presence of a company based in Italy. Our website will include a general e-mail box link for additional info. requests, color photos of our operation, a link to our parent company's website, a video, a mission statement, a description of our capabilities.Our internet presence will be on a B2B basis, to include a map of our location and contact information.

Target Market(s)

Businesses seeking contract manufacturer in the US nutraceutical industry.

Industry/Entity Type

Manufacturer

Number of Pages Required

3 page

Font styles to use
Sans Serif

Colors
3176b5
f04a50

Requirements
Must have
• Colors, as described in project description section. Three pages minimum - one to define what we do/location/contact info,/links to affiliated companies, one to showcase certifications, one to provide photos. We are open to having additional pages as suggested, if necessary. Our website for contacts info: www.kelvoranto-us.com .
• Link to our general email box: info@kelvoranto-us.com
• Pantone colors detailed in project description.
• HTTPS secure presence
Nice to have
• TBD
Should not have
• PROFANITY

```html
<!DOCTYPE html>
<html lang="en">
<head>
<meta charset="utf-8">
<title>Kelvoranto US — Nutraceutical Contract Manufacturer</title>
<link href="https://fonts.googleapis.com/css2?family=Lato:wght@300;400;700;900&display=swap" rel="stylesheet">
<style>
:root{
  --blue:#3176b5;
  --blue-deep:#2a68a6;
  --red:#f04a50;
  --white:#ffffff;
  --ink:#2b2b2b;
  --text:#555a60;
  --muted:#8a9099;
  --map:#e6e4df;
}
*{margin:0;padding:0;box-sizing:border-box}
html,body{width:1200px;height:2281px;overflow:hidden}
body{font-family:'Lato',Arial,sans-serif;background:var(--white);color:var(--text);position:relative}
.abs{position:absolute}

/* top bar */
.topbar{left:0;top:0;width:1200px;height:24px;background:var(--blue);color:var(--white);font-size:9px;font-weight:700}
.topbar .item{top:6px;display:flex;align-items:center;gap:5px}
.topbar .addr{left:626px}
.topbar .phone{left:820px}
.topbar .dots{left:918px;top:8px;display:flex;gap:9px}
.topbar .dots span{width:7px;height:7px;border-radius:50%;background:var(--white);display:block}

/* header */
.header{left:0;top:24px;width:1200px;height:84px;background:var(--white)}
.brand{font-weight:700;color:var(--blue);font-size:24px;letter-spacing:.3px;display:flex;align-items:center;gap:8px}
.brand .mark{width:12px;height:12px;border-radius:50%;background:var(--red)}
.header .brand{left:240px;top:28px}
.nav{display:flex;font-size:11px;font-weight:400;color:var(--ink);letter-spacing:.2px}
.header .nav{left:575px;top:37px;gap:34px}

/* hero */
.hero{left:0;top:108px;width:1200px;height:359px;overflow:hidden;background:var(--blue)}
.hero svg{position:absolute;left:0;top:0}
.hero .kicker{left:240px;top:82px;color:var(--white);font-size:28px;font-weight:400;line-height:1}
.hero .title{left:240px;top:110px;color:var(--white);font-size:43px;font-weight:700;line-height:1}
.hero .sub{left:240px;top:153px;color:var(--white);font-size:30px;font-weight:400;line-height:1}
.hero .lede{left:240px;top:201px;width:340px;color:var(--white);font-size:11.5px;line-height:18px}
.btn-outline{border:1px solid var(--white);color:var(--white);font-size:11px;border-radius:3px;display:flex;align-items:center;justify-content:center;letter-spacing:.3px}
.hero .btn-outline{left:240px;top:269px;width:114px;height:28px}
.hero .pager{left:578px;top:335px;display:flex;gap:11px}
.hero .pager span{width:8px;height:8px;border-radius:50%;background:var(--white);display:block}

/* mission */
.mission{left:240px;top:517px;width:720px;text-align:center;font-size:21px;font-weight:300;line-height:31px;color:var(--ink)}
.mission strong{color:var(--blue);font-weight:700}
.accent-bar{width:36px;height:6px;border-radius:3px;background:var(--red)}
.mission-bar{left:582px;top:624px}

/* about */
.photo-shadow{background:var(--blue)}
.about-shadow{left:248px;top:697px;width:356px;height:327px}
.about-photo{left:240px;top:687px;width:353px;height:323px;background:linear-gradient(135deg,#5c6e82 0%,#b7c3cf 45%,#e8eef3 100%)}
.eyebrow{font-size:12px;font-weight:300}
.heading{font-size:31px;font-weight:700;color:var(--ink);line-height:1;letter-spacing:.3px}
.copy{font-size:11.5px;line-height:19.5px;font-weight:300;color:var(--text)}
.copy p+p{margin-top:19px}
.about-eyebrow{left:617px;top:703px;color:var(--blue)}
.about-heading{left:615px;top:720px}
.about-copy{left:617px;top:773px;width:345px}

/* what we do */
.services{left:0;top:1068px;width:1200px;height:410px}
.services svg{position:absolute;left:0;top:0}
.services .heading-w{left:0;top:66px;width:1200px;text-align:center;color:var(--white);font-size:31px;font-weight:400;letter-spacing:.3px}
.services .col{top:122px;width:345px;color:var(--white);font-size:11.5px;line-height:19.5px;font-weight:300}
.services .col p+p{margin-top:19px}
.services .col strong{font-weight:700}
.services .col-left{left:241px}
.services .col-right{left:617px}

/* how we do */
.video{left:240px;top:1529px;width:368px;height:206px;background:linear-gradient(120deg,#6f7e8c 0%,#c8d0d8 50%,#e9e1c4 100%)}
.video svg{position:absolute;left:158px;top:77px}
.how-eyebrow{left:635px;top:1537px;color:var(--red)}
.how-heading{left:633px;top:1552px}
.how-copy{left:635px;top:1600px;width:330px}

/* cta */
.cta{left:0;top:1801px;width:1200px;height:90px;background:var(--red)}
.cta .eyebrow{left:303px;top:21px;color:var(--white)}
.cta .cta-title{left:302px;top:35px;color:var(--white);font-size:27px;font-weight:700;letter-spacing:.3px}
.cta .btn-outline{left:794px;top:30px;width:114px;height:28px}

/* map */
.map{left:0;top:1891px;width:1200px;height:293px;background:linear-gradient(160deg,#ece9e3 0%,#e2e2dc 60%,#d9e4e6 100%)}

/* footer */
.footer{left:0;top:2184px;width:1200px;height:61px;background:var(--blue)}
.footer .brand{left:243px;top:17px;color:var(--white);font-size:21px}
.footer .brand .mark{background:var(--white)}
.footer .nav{left:601px;top:24px;gap:24px;color:var(--white);font-size:10px}
.copyright{left:0;top:2257px;width:1200px;text-align:center;font-size:9.5px;color:var(--ink)}
</style>
</head>
<body>

<div class="topbar abs">
  <div class="item addr abs">
    <svg width="8" height="10" viewBox="0 0 8 10"><path d="M4 0a4 4 0 0 0-4 4c0 3 4 6 4 6s4-3 4-6a4 4 0 0 0-4-4zm0 5.5A1.5 1.5 0 1 1 4 2.5a1.5 1.5 0 0 1 0 3z" fill="#fff"/></svg>
    240 Harbor Lane, Millbrook, NJ 08000 USA
  </div>
  <div class="item phone abs">
    <svg width="9" height="9" viewBox="0 0 10 10"><path d="M2 0l2 2.3-1 1.3a6 6 0 0 0 3.4 3.4l1.3-1L10 8l-1.2 2C4 10 0 6 0 1.2z" fill="#fff"/></svg>
    +1 (555) 014-2290
  </div>
  <div class="dots abs"><span></span><span></span><span></span></div>
</div>

<header class="header abs">
  <div class="brand abs"><span class="mark"></span>Kelvoranto US</div>
  <nav class="nav abs"><span>HOME</span><span>WHAT WE DO</span><span>ABOUT US</span><span>CERTIFICATIONS</span><span>CONTACT US</span></nav>
</header>

<section class="hero abs">
  <svg width="1200" height="359" viewBox="0 0 1200 359">
    <rect width="1200" height="359" fill="var(--blue)"/>
    <polygon points="0,0 300,0 150,180 0,60" fill="#3a80bf" opacity=".5"/>
    <polygon points="300,0 590,0 450,230" fill="#2d6eac" opacity=".6"/>
    <polygon points="0,180 200,359 0,359" fill="#3a80bf" opacity=".5"/>
    <polygon points="592,0 608,0 686,359 670,359" fill="var(--red)"/>
    <polygon points="608,0 1200,0 1200,359 686,359" fill="url(#labFill)" role="img" aria-label="Photo of laboratory precision balances and instruments on a bench"/>
    <defs>
      <linearGradient id="labFill" x1="0" y1="0" x2="1" y2="1">
        <stop offset="0" stop-color="#d9dde1"/>
        <stop offset=".5" stop-color="#b8bfc6"/>
        <stop offset="1" stop-color="#7d858d"/>
      </linearGradient>
    </defs>
  </svg>
  <div class="kicker abs">SPECIALIZING IN</div>
  <h1 class="title abs">NUTRACEUTICAL</h1>
  <div class="sub abs">PRODUCTS</div>
  <p class="lede abs">Kelvoranto US LLC is a contract manufacturer for the food supplements market, producing exclusively for third parties.</p>
  <a class="btn-outline abs">VIEW MORE</a>
  <div class="pager abs"><span></span><span></span><span></span></div>
</section>

<p class="mission abs">The mission of Kelvoranto US is to be the <strong>premier contract manufacturer of dietary supplements in the United States</strong>, offering quality and excellence to our customers.</p>
<div class="accent-bar mission-bar abs"></div>

<div class="photo-shadow about-shadow abs"></div>
<div class="about-photo abs" role="img" aria-label="Photo of an operator in protective clothing using a production control panel"></div>
<div class="eyebrow about-eyebrow abs">The Contract Manufacturer</div>
<h2 class="heading about-heading abs">KELVORANTO US</h2>
<div class="copy about-copy abs">
  <p>Lorem ipsum dolor sit amet, consectetuer adipiscing elit. Aenean commodo ligula eget dolor. Aenean massa. Cum sociis natoque penatibus et magnis dis parturient montes, nascetur ridiculus mus.</p>
  <p>Donec quam felis, ultricies nec, pellentesque eu, pretium quis, sem. Nulla consequat massa quis enim. Donec pede justo, fringilla vel, aliquet nec, vulputate eget, arcu. In enim justo, rhoncus ut, imperdiet a, venenatis vitae, justo.</p>
  <p>Nullam dictum felis eu pede mollis pretium. Integer tincidunt. Cras dapibus. Vivamus elementum semper nisi.</p>
</div>

<section class="services abs">
  <svg width="1200" height="410" viewBox="0 0 1200 410">
    <defs>
      <linearGradient id="bandFill" x1="0" y1="0" x2="1" y2="0">
        <stop offset="0" stop-color="#2f6fae"/>
        <stop offset=".5" stop-color="#3a7cba"/>
        <stop offset="1" stop-color="#2f6fae"/>
      </linearGradient>
    </defs>
    <polygon points="0,22 1200,4 1200,404 0,386" fill="var(--red)"/>
    <polygon points="0,22 1200,4 1200,397 0,381" fill="url(#bandFill)" role="img" aria-label="Photo of a clean production hall tinted in brand blue"/>
  </svg>
  <h2 class="heading-w abs">WHAT WE DO</h2>
  <div class="col col-left abs">
    <p><strong>Lorem ipsum dolor sit amet</strong>, consectetuer adipiscing elit. Aenean commodo ligula eget dolor. Aenean massa. Cum sociis natoque penatibus et magnis dis parturient montes, nascetur ridiculus mus.</p>
    <p><strong>Donec quam felis</strong>, ultricies nec, pellentesque eu, pretium quis, sem. Nulla consequat massa quis enim. Donec pede justo, fringilla vel, aliquet nec, vulputate eget, arcu. In enim justo, rhoncus ut, imperdiet a, venenatis vitae, justo.</p>
    <p><strong>Nullam dictum felis</strong> eu pede mollis pretium. Integer tincidunt. Cras dapibus. Vivamus elementum semper nisi.</p>
  </div>
  <div class="col col-right abs">
    <p><strong>Lorem ipsum</strong> dolor sit amet, consectetuer adipiscing elit. Aenean commodo ligula eget dolor. Aenean massa. Cum sociis natoque penatibus et magnis dis parturient montes, nascetur ridiculus mus.</p>
    <p><strong>Donec quam felis</strong>, ultricies nec, pellentesque eu, pretium quis, sem. Nulla consequat massa quis enim. Donec pede justo, fringilla vel, aliquet nec, vulputate eget, arcu. In enim justo, rhoncus ut, imperdiet a, venenatis vitae, justo.</p>
    <p><strong>Cum sociis</strong> natoque penatibus et magnis dis parturient montes, nascetur ridiculus mus.</p>
  </div>
</section>

<div class="video abs" role="img" aria-label="Video still of a blister packaging machine on the production line">
  <svg width="52" height="52" viewBox="0 0 52 52"><circle cx="26" cy="26" r="24" fill="none" stroke="#fff" stroke-width="3" opacity=".85"/><polygon points="20,15 37,26 20,37" fill="#fff" opacity=".85"/></svg>
</div>
<div class="eyebrow how-eyebrow abs">Kelvoranto US</div>
<h2 class="heading how-heading abs">HOW WE DO</h2>
<div class="copy how-copy abs">
  <p>Lorem ipsum dolor sit amet, consectetuer adipiscing elit. Aenean commodo ligula eget dolor. Aenean massa. Cum sociis natoque penatibus et magnis dis parturient montes, nascetur ridiculus mus.</p>
  <p>Donec quam felis, ultricies nec, pellentesque eu, pretium quis, sem. Nulla consequat massa quis enim.</p>
</div>

<section class="cta abs">
  <div class="eyebrow abs">Kelvoranto US</div>
  <h2 class="cta-title abs">WE ARE THE SOLUTION</h2>
  <a class="btn-outline abs">CONTACT NOW</a>
</section>

<div class="map abs" role="img" aria-label="Street map showing the company location in New Jersey"></div>

<footer class="footer abs">
  <div class="brand abs"><span class="mark"></span>Kelvoranto US</div>
  <nav class="nav abs"><span>HOME</span><span>WHAT WE DO</span><span>ABOUT US</span><span>CERTIFICATIONS</span><span>CONTACT US</span></nav>
</footer>
<p class="copyright abs">© Copyright 2018 Kelvoranto US . All Right Reserved</p>

</body>
</html>
```